Brightway Gate works Business cards/Stationery
Business cards and stationery
Brightway Gate works Business cards/Stationery -
Creative Brief
Use specific fonts
Whatever you think looks best
Professional
Paul Hendley
Owner
248 Marlow Ridge Rd. Easley, SC 29642
Brightwaygateworks@mailnest.net
www.Brightwaygateworks.net
Use tagline: A Warm Welcome At Every Gate
I would like to see something unique with the logo on the back.

```html
<!DOCTYPE html>
<html lang="en">
<head>
<meta charset="utf-8">
<title>Brightway Gate works – Business Card</title>
<link href="https://fonts.googleapis.com/css2?family=Open+Sans:ital,wght@0,400;0,600;0,700;1,600;1,700&display=swap" rel="stylesheet">
<style>
  :root {
    --page-bg: #e9e4dc;
    --card-bg: #ffffff;
    --ink: #333333;
    --ink-soft: #4a4a4a;
    --brand-red: #8c1f22;
    --swoosh: #2b2b2b;
    --divider: #c9c9c9;
  }
  * { box-sizing: border-box; margin: 0; padding: 0; }
  html, body { width: 1200px; height: 965px; overflow: hidden; }
  body {
    background: var(--page-bg);
    font-family: "Open Sans", Arial, sans-serif;
    color: var(--ink);
    position: relative;
  }
  .card {
    position: absolute;
    left: 100px; top: 193px;
    width: 1000px; height: 580px;
    background: var(--card-bg);
    border-radius: 34px;
    overflow: hidden;
    box-shadow: 0 6px 18px rgba(0,0,0,0.25);
  }
  .brand {
    position: absolute;
    left: 118px; top: 52px;
    display: flex; align-items: center; gap: 22px;
  }
  .brand-mark {
    width: 58px; height: 58px;
    background: var(--brand-red);
  }
  .brand-name {
    font-weight: 700;
    font-size: 56px;
    letter-spacing: 1px;
    color: var(--ink);
    line-height: 1;
  }
  .holder {
    position: absolute;
    left: 40px; top: 182px;
    width: 300px;
    text-align: right;
  }
  .holder-name {
    font-weight: 700;
    font-size: 38px;
    color: var(--brand-red);
    line-height: 1.2;
  }
  .holder-role {
    font-style: italic;
    font-weight: 700;
    font-size: 24px;
    color: var(--ink);
    margin-bottom: 16px;
  }
  .holder-address {
    font-size: 27px;
    line-height: 1.45;
    color: var(--ink-soft);
  }
  .divider {
    position: absolute;
    left: 374px; top: 182px;
    width: 2px; height: 180px;
    background: var(--divider);
  }
  .contacts {
    position: absolute;
    left: 408px; top: 190px;
    list-style: none;
  }
  .contacts li {
    display: flex; align-items: center; gap: 16px;
    font-size: 27px;
    line-height: 1;
    height: 41px;
    color: var(--ink-soft);
  }
  .contacts svg { width: 26px; height: 26px; flex: none; }
  .footer-band {
    position: absolute; left: 0; bottom: 0;
    width: 1000px; height: 200px;
  }
  .tagline {
    position: absolute;
    left: 0; right: 0; top: 470px;
    text-align: center;
    font-style: italic;
    font-weight: 700;
    font-size: 30px;
    letter-spacing: 0.5px;
    color: #ffffff;
  }
</style>
</head>
<body>
  <article class="card">
    <div class="brand">
      <span class="brand-mark"></span>
      <span class="brand-name">Brightway Gate works</span>
    </div>

    <div class="holder">
      <p class="holder-name">Paul Hendley</p>
      <p class="holder-role">Owner</p>
      <p class="holder-address">248 Marlow Ridge Rd.<br>Easley, SC 29642</p>
    </div>

    <span class="divider"></span>

    <ul class="contacts">
      <li>
        <svg viewBox="0 0 24 24"><path fill="#8c1f22" d="M6.6 10.8a15 15 0 0 0 6.6 6.6l2.2-2.2c.3-.3.7-.4 1-.2 1.1.4 2.3.6 3.6.6.6 0 1 .4 1 1V20c0 .6-.4 1-1 1A17 17 0 0 1 3 4c0-.6.4-1 1-1h3.5c.6 0 1 .4 1 1 0 1.3.2 2.5.6 3.6.1.3 0 .7-.2 1z"/></svg>
        (864)-555-0142
      </li>
      <li>
        <svg viewBox="0 0 24 24"><path fill="#8c1f22" d="M7 3h10v5H7zM4 9h16a2 2 0 0 1 2 2v6h-4v4H6v-4H2v-6a2 2 0 0 1 2-2zm4 7v3h8v-3z"/></svg>
        (864)-555-0187
      </li>
      <li>
        <svg viewBox="0 0 24 24"><text x="12" y="19" text-anchor="middle" font-family="Open Sans, Arial, sans-serif" font-weight="700" font-size="21" fill="#8c1f22">@</text></svg>
        Brightwaygateworks@mailnest.net
      </li>
      <li>
        <svg viewBox="0 0 24 24" fill="none" stroke="#8c1f22" stroke-width="1.8"><circle cx="12" cy="12" r="9"/><ellipse cx="12" cy="12" rx="4" ry="9"/><path d="M3 12h18M5 7h14M5 17h14"/></svg>
        www.Brightwaygateworks.net
      </li>
    </ul>

    <svg class="footer-band" viewBox="0 0 1000 200" preserveAspectRatio="none">
      <defs>
        <linearGradient id="bandFill" x1="0" y1="0" x2="0" y2="1">
          <stop offset="0" stop-color="#7a1a1e"/>
          <stop offset="0.55" stop-color="#5a1114"/>
          <stop offset="1" stop-color="#3a0a0c"/>
        </linearGradient>
      </defs>
      <path d="M0 52 C 260 24, 600 12, 1000 2 L1000 28 C 620 30, 300 48, 0 80 Z" fill="#2b2b2b"/>
      <path d="M0 80 C 300 48, 620 30, 1000 28 L1000 200 L0 200 Z" fill="url(#bandFill)"/>
    </svg>

    <p class="tagline">A Warm Welcome At Every Gate</p>
  </article>
</body>
</html>
```